Mortgage Loan Program(s) for Furloughed Federal Government Workers

Mortgage Loan Program(s)
For
Furloughed Federal Government Workers

* Preserve Your Credit Rating
* Receive Cash out to Increase Savings or Consolidate Bills
* Close in 30 Days or Less
* FHA and Conventional Loan Programs
* Very Competitive Rates Available
* DC & MD Properties Only

You deserve better. Contact us today....

Office (800) 446-2917 x24
Cell (240) 958-2043
Email mpelton@brightkeyhome.example

Marcus Pelton
Brightkey Financial Services, Inc.
NMLS #518374 / #60471

Target Market(s)

```html
<!DOCTYPE html>
<html lang="en">
<head>
<meta charset="utf-8">
<title>Mortgage Loan Programs for Furloughed Federal Government Workers</title>
<link href="https://fonts.googleapis.com/css2?family=Oswald:wght@500;600&family=Cinzel:wght@500;700&family=Lato:ital,wght@0,400;0,700;1,400;1,700;1,900&display=swap" rel="stylesheet">
<style>
  :root {
    --navy: #1a2f7e;
    --navy-deep: #0f1f5c;
    --band-blue: #2b4c9e;
    --gold: #b29a2c;
    --gold-light: #c9b13e;
    --cream: #f8ef92;
    --ink: #1c1c30;
    --white: #ffffff;
    --label-gold: #e9cf4a;
  }
  * { box-sizing: border-box; margin: 0; padding: 0; }
  html, body { width: 902px; height: 1200px; overflow: hidden; background: #ffffff; }
  .flyer { position: relative; width: 902px; height: 1200px; overflow: hidden; font-family: 'Lato', sans-serif; }
  .backdrop { position: absolute; inset: 0; }
  .brand { position: absolute; left: 64px; top: 96px; display: flex; align-items: center; gap: 10px;
    font-family: 'Lato', sans-serif; font-weight: 700; font-size: 20px; line-height: 1; color: var(--navy); white-space: nowrap; }
  .brand-dot { width: 24px; height: 24px; border-radius: 50%; background: var(--gold); flex: none; }
  .headline { position: absolute; left: 42px; top: 330px; color: var(--cream); }
  .headline-main { font-family: 'Oswald', sans-serif; font-weight: 600; font-size: 70px; line-height: 1; letter-spacing: 1px; }
  .headline-sub { font-family: 'Oswald', sans-serif; font-weight: 500; font-size: 36px; line-height: 1; margin-top: 22px; letter-spacing: .5px; }
  .headline-sub .for { color: var(--white); }
  .audience { position: absolute; left: 42px; top: 478px; color: var(--white);
    font-family: 'Cinzel', serif; font-weight: 500; font-size: 49px; line-height: 58px; }
  .photo { position: absolute; border-radius: 50%; border: 5px solid var(--white); }
  .photo-worried { left: 20px; top: 672px; width: 280px; height: 280px; background: radial-gradient(circle at 45% 40%, #d9cfc6, #8f7c70); }
  .photo-couple { left: 272px; top: 622px; width: 214px; height: 214px; background: radial-gradient(circle at 50% 45%, #c9c2bc, #6d665f); }
  .glow { position: absolute; left: 300px; top: 840px; width: 280px; height: 160px; border-radius: 50%;
    background: radial-gradient(ellipse at 50% 40%, rgba(255,236,150,.75), rgba(201,177,62,0) 70%); }
  .stamp { position: absolute; left: 560px; top: 648px; padding: 2px 14px; border: 4px solid var(--white); border-radius: 6px;
    color: var(--white); font-family: 'Cinzel', serif; font-weight: 700; font-size: 44px; letter-spacing: 1px; transform: rotate(-5deg); line-height: 1.1; }
  .benefits { position: absolute; left: 494px; top: 752px; list-style: none; color: var(--ink);
    font-style: italic; font-weight: 700; font-size: 20px; line-height: 24px; }
  .benefits li { position: relative; padding-left: 26px; margin-bottom: 11px; }
  .benefits li::before { content: ""; position: absolute; left: 0; top: 5px; width: 14px; height: 14px; border-radius: 50%; background: var(--white); }
  .portrait { position: absolute; left: 44px; top: 997px; width: 136px; height: 155px; border: 3px solid var(--gold-light);
    background: linear-gradient(160deg, #6f85a6 0%, #3b4d6e 60%, #1e2437 100%); }
  .agent { position: absolute; left: 196px; top: 1040px; color: var(--white); }
  .agent-name { font-weight: 700; font-size: 28px; line-height: 34px; }
  .agent-meta { font-style: italic; font-weight: 700; font-size: 16px; line-height: 20px; }
  .cta { position: absolute; left: 522px; top: 1024px; color: var(--navy-deep); font-style: italic; font-size: 19px; }
  .cta strong { font-weight: 700; }
  .contact { position: absolute; left: 531px; top: 1070px; list-style: none; color: var(--white);
    font-style: italic; font-weight: 700; font-size: 19px; line-height: 30px; white-space: nowrap; }
  .contact .label { color: var(--label-gold); font-weight: 400; }
</style>
</head>
<body>
<main class="flyer">
  <svg class="backdrop" viewBox="0 0 902 1200" width="902" height="1200" aria-hidden="true">
    <defs>
      <linearGradient id="capitol-tone" x1="0" y1="0" x2="0" y2="1">
        <stop offset="0" stop-color="#1d3f8f"/>
        <stop offset=".6" stop-color="#4a68a8"/>
        <stop offset=".85" stop-color="#8a6b45"/>
        <stop offset="1" stop-color="#3c2d22"/>
      </linearGradient>
      <linearGradient id="body-blue" x1="0" y1="0" x2="1" y2="1">
        <stop offset="0" stop-color="#1e3b8c"/>
        <stop offset="1" stop-color="#14296e"/>
      </linearGradient>
    </defs>
    <rect width="902" height="1200" fill="#ffffff"/>
    <!-- main blue field, following the photo frame's curved edge -->
    <path d="M0,250 Q220,200 392,330 Q420,120 560,0 L902,0 L902,1000 L0,1000 Z" fill="url(#body-blue)"/>
    <!-- gold swoosh under the brand -->
    <path d="M0,246 Q230,196 392,330" fill="none" stroke="var(--gold)" stroke-width="12"/>
    <!-- top-right photo frame -->
    <path d="M560,0 Q420,120 391,330 Q380,380 420,395 Q620,470 902,390 L902,0 Z" fill="#ffffff"/>
    <path d="M583,0 Q440,120 408,325 Q402,372 440,382 Q630,450 902,378 L902,0 Z" fill="url(#capitol-tone)" role="img" aria-label="Photo of the US Capitol dome lit at dusk"/>
    <path d="M560,0 Q420,120 391,330" fill="none" stroke="var(--gold)" stroke-width="10"/>
    <!-- gold lower section -->
    <path d="M0,720 Q300,640 560,630 Q760,620 902,590 L902,1000 L0,1000 Z" fill="#ffffff"/>
    <path d="M0,740 Q300,660 560,650 Q760,640 902,610 L902,1000 L0,1000 Z" fill="var(--gold)"/>
    <!-- bottom band -->
    <rect x="0" y="999" width="902" height="201" fill="var(--band-blue)"/>
    <path d="M460,1054 L902,1054 L902,1200 L560,1200 Z" fill="var(--navy-deep)"/>
    <path d="M409,1017 L902,1017 L902,1054 L440,1054 Z" fill="#ffffff"/>
  </svg>

  <div class="brand"><span class="brand-dot"></span>Brightkey Financial Services, Inc.</div>

  <div class="headline">
    <div class="headline-main">MORTGAGE</div>
    <div class="headline-sub">LOAN PROGRAM(S) <span class="for">FOR</span></div>
  </div>
  <h1 class="audience">Furloughed Federal<br>Government Workers</h1>

  <div class="glow" role="img" aria-label="Silhouette of a person with raised arms against a bright sunrise"></div>
  <div class="photo photo-worried" role="img" aria-label="Photo of a stressed couple going over bills, holding a help sign"></div>
  <div class="photo photo-couple" role="img" aria-label="Photo of a couple reviewing paperwork together"></div>

  <div class="stamp">APPROVED</div>

  <ul class="benefits">
    <li>Preserve Your Credit Rating</li>
    <li>Receive Cash out to Increase Savings<br>or Consolidate Bills</li>
    <li>Close in 30 Days or Less</li>
    <li>FHA and Conventional Loan Programs</li>
    <li>Very Competitive Rates Available</li>
    <li>DC &amp; MD Properties Only</li>
  </ul>

  <div class="portrait" role="img" aria-label="Portrait photo of the loan officer in a suit"></div>
  <div class="agent">
    <div class="agent-name">Marcus Pelton</div>
    <div class="agent-meta">Brightkey Financial Services, Inc.</div>
    <div class="agent-meta">NMLS #518374 / #60471</div>
  </div>

  <p class="cta"><strong>YOU DESERVE BETTER.</strong> Contact us today....</p>
  <ul class="contact">
    <li><span class="label">Office</span> (800) 446-2917 x24</li>
    <li><span class="label">Cell</span> (240) 958-2043</li>
    <li><span class="label">Email</span> mpelton@brightkeyhome.example</li>
  </ul>
</main>
</body>
</html>
```